Waste Oil Filter collection & disposal

Basically I need a 1 page website for the business called Brenmoor Waste Solutions.
We are a environmental service provider and we collect and dispose of waste oil filters to protect the environment from hazardous waste oil products.

This is the link to our current website: www.brenmoorwaste.co.nz

we want it to look fresh and better than our current website. we may potentially look at getting a new logo designed and are open to ideas/designs if you have any.

Industry/Entity Type

Business

Logo Text

Brenmoor Waste Solutions

Number of Pages Required

1 page

Requirements
Must have
• same colours as current website.
• description of what service we provide please refer to leaflet attached

```html
<!DOCTYPE html>
<html lang="en">
<head>
<meta charset="utf-8">
<title>Brenmoor Waste Solutions</title>
<link href="https://fonts.googleapis.com/css2?family=Open+Sans:wght@300;400;600;700&display=swap" rel="stylesheet">
<style>
:root{
  --page:#ececec;
  --ink:#222222;
  --muted:#6e6e6e;
  --icon:#5a5a5a;
  --dark:#4a4646;
  --field:#3a3636;
  --field-line:#6a6464;
  --white:#ffffff;
  --green:#4dbb4a;
  --green-deep:#1f7a4a;
}
*{margin:0;padding:0;box-sizing:border-box}
html,body{width:1200px;height:3613px;overflow:hidden;background:var(--page)}
body{font-family:"Open Sans",Arial,sans-serif;color:var(--ink);position:relative}
.canvas{position:relative;width:1200px;height:3613px;overflow:hidden;background:var(--page)}
.shapes{position:absolute;left:0;top:0}
.nav{position:absolute;top:56px;left:0;width:1200px;font-size:14px;font-weight:700;color:var(--white);letter-spacing:.5px}
.nav a{position:absolute;color:inherit;text-decoration:none}
.brand{position:absolute;left:0;width:1200px;top:262px;text-align:center;color:var(--white)}
.brand-name{font-size:46px;font-weight:700;letter-spacing:.5px}
.brand-tag{font-size:18px;font-weight:600;margin-top:18px}
.section-title{position:absolute;left:232px;font-size:46px;font-weight:700;color:var(--ink)}
.about-lead{position:absolute;left:228px;top:975px;font-size:132px;font-weight:300;color:var(--ink)}
.gallery-link{position:absolute;left:522px;top:1478px;font-size:36px;font-weight:600;color:var(--white)}
.gallery-link::after{content:"";display:block;width:126px;height:4px;background:var(--white);margin-top:4px}
.icon{position:absolute}
.step-title{position:absolute;top:2210px;font-size:40px;font-weight:400;color:var(--ink)}
.process-text{position:absolute;left:235px;top:2318px;font-size:17px;line-height:20px;color:var(--muted)}
.oil-text{position:absolute;left:691px;width:400px;top:2310px;font-size:17px;line-height:21px;color:var(--muted);text-align:center}
.oil-text .figure{font-size:28px;color:var(--ink);letter-spacing:2px}
.contact-title{position:absolute;left:232px;top:2998px;font-size:46px;font-weight:700;color:var(--white)}
.contact-sub{position:absolute;left:222px;top:3062px;font-size:25px;color:var(--white)}
.contact-brand{position:absolute;left:670px;top:2993px;display:flex;align-items:center;gap:14px;color:var(--green);font-size:30px;font-weight:700;line-height:1.1;width:420px}
.contact-brand .mark{width:26px;height:26px;background:var(--green);flex:none}
.contact-line{position:absolute;display:flex;align-items:flex-start;gap:18px;color:var(--white);font-weight:700}
.contact-line.phone{left:178px;top:3188px;font-size:27px}
.contact-line.address{left:190px;top:3288px;font-size:19px;line-height:26px}
.field{position:absolute;height:33px;background:var(--field);border:2px solid var(--field-line);color:var(--white);font-size:17px;padding:3px 8px}
.field.message{height:103px}
.send{position:absolute;left:890px;top:3425px;font-size:20px;font-weight:700;color:var(--white)}
</style>
</head>
<body>
<div class="canvas">
  <svg class="shapes" width="1200" height="3613" viewBox="0 0 1200 3613">
    <defs>
      <linearGradient id="heroTone" x1="0" y1="0" x2="1" y2="1">
        <stop offset="0" stop-color="#3f6b4e"/>
        <stop offset=".5" stop-color="#5f8d6f"/>
        <stop offset="1" stop-color="#2e5a3c"/>
      </linearGradient>
      <linearGradient id="panelA" x1="0" y1="0" x2="0" y2="1"><stop offset="0" stop-color="#4ea65c"/><stop offset="1" stop-color="#2f8a45"/></linearGradient>
      <linearGradient id="panelB" x1="0" y1="0" x2="0" y2="1"><stop offset="0" stop-color="#3f8f8c"/><stop offset="1" stop-color="#2f7272"/></linearGradient>
      <linearGradient id="panelC" x1="0" y1="0" x2="0" y2="1"><stop offset="0" stop-color="#6f8e76"/><stop offset="1" stop-color="#4f6e5a"/></linearGradient>
      <linearGradient id="panelD" x1="0" y1="0" x2="0" y2="1"><stop offset="0" stop-color="#3ca65a"/><stop offset="1" stop-color="#2a8a48"/></linearGradient>
    </defs>
    <polygon points="0,0 1200,0 1200,499 0,894" fill="url(#heroTone)" role="img" aria-label="Photo of a green and white filter collection truck parked on grass, tinted green"/>
    <g role="img" aria-label="Gallery strip of photos: collection truck, processing plant, crushed filters and machinery">
      <polygon points="0,1448 320,1368 320,1828 0,1905" fill="url(#panelA)"/>
      <polygon points="320,1368 680,1278 680,1738 320,1828" fill="url(#panelB)"/>
      <polygon points="680,1278 940,1213 940,1675 680,1738" fill="url(#panelC)"/>
      <polygon points="940,1213 1200,1148 1200,1480 940,1675" fill="url(#panelD)"/>
    </g>
    <polygon points="0,2966 1200,2680 1200,3613 0,3613" fill="var(--dark)"/>
  </svg>

  <nav class="nav">
    <a style="left:701px">ABOUT US</a>
    <a style="left:846px">HOW IT WORKS</a>
    <a style="left:1039px">CONTACT US</a>
  </nav>

  <header class="brand">
    <div class="brand-name">Brenmoor Waste Solutions</div>
    <div class="brand-tag">Oil Filter Collection &amp; Disposal Service</div>
  </header>

  <h2 class="section-title" style="top:875px">ABOUT US</h2>
  <p class="about-lead">Filter</p>

  <a class="gallery-link">Visit Gallery</a>

  <h2 class="section-title" style="top:1908px">HOW IT WORKS</h2>

  <svg class="icon" style="left:305px;top:2085px" width="60" height="95" viewBox="0 0 60 95" aria-hidden="true">
    <path d="M4 0h14v22h24V0h14v30l-12 12v53H16V42L4 30z" fill="var(--icon)"/>
  </svg>
  <svg class="icon" style="left:858px;top:2075px" width="70" height="105" viewBox="0 0 70 105" aria-hidden="true">
    <path d="M28 40 C20 60 8 72 8 86 a20 20 0 0 0 40 0 C48 72 36 60 28 40z" fill="var(--icon)"/>
    <path d="M56 0 C52 10 46 16 46 23 a10 10 0 0 0 20 0 C66 16 60 10 56 0z" fill="var(--icon)"/>
  </svg>

  <h3 class="step-title" style="left:235px">TheProcess</h3>
  <h3 class="step-title" style="left:688px">What Happens to the Oil</h3>

  <p class="process-text">
    Filters are collected and transported back<br>to the processing plant<br>At the processing plant they are:<br>Drained<br>Sorted<br>Drained again<br>Crushed into bricks<br>Drained a third time<br>Stacked ready for Metal Recycling
  </p>
  <p class="oil-text">
    All residual oil is collected into our<br>tank and then recycled.<br>Currently we are processing<br>over <span class="figure">2,000</span><br>litres of oil a month.
  </p>

  <h2 class="contact-title">CONTACT US</h2>
  <p class="contact-sub">We appreciate this very Much</p>
  <div class="contact-brand"><span class="mark"></span><span>Brenmoor Waste Solutions</span></div>

  <div class="contact-line phone">
    <svg width="36" height="36" viewBox="0 0 24 24" aria-hidden="true"><path d="M6.6 10.8a15 15 0 0 0 6.6 6.6l2.2-2.2c.3-.3.7-.4 1-.2 1.1.4 2.3.6 3.6.6.6 0 1 .4 1 1V20c0 .6-.4 1-1 1A17 17 0 0 1 3 4c0-.6.4-1 1-1h3.5c.6 0 1 .4 1 1 0 1.3.2 2.5.6 3.6.1.3 0 .7-.2 1z" fill="var(--white)"/></svg>
    <span>06 555 0147</span>
  </div>
  <div class="contact-line address">
    <svg width="30" height="40" viewBox="0 0 24 32" aria-hidden="true"><path d="M12 0a11 11 0 0 0-11 11c0 8 11 21 11 21s11-13 11-21A11 11 0 0 0 12 0zm0 16a5 5 0 1 1 0-10 5 5 0 0 1 0 10z" fill="var(--white)"/></svg>
    <span>Harlow Mills, Ashdene 4872<br>, New Zealand</span>
  </div>

  <form>
    <div class="field" style="left:515px;top:3162px;width:186px">Name</div>
    <div class="field" style="left:756px;top:3162px;width:193px">Email</div>
    <div class="field" style="left:515px;top:3227px;width:186px">Phone</div>
    <div class="field" style="left:756px;top:3227px;width:193px">Subject</div>
    <div class="field message" style="left:515px;top:3291px;width:434px">Message</div>
    <span class="send">Send</span>
  </form>
</div>
</body>
</html>
```